2-Sided Law Firm Business Card

This is the second phase of a law firm "rebrand project" in which I'm changing my firm's name to "Brockwyn Law PLLC." The first phase was a logo contest -- I will be updating this project sometime tomorrow with the winning logo design.

The business card will need to include, on its reverse side, the firm's logo and tag line, "Legal Counsel for the Innovative Company," on a darker background whose color is consistent with the logo design.

The face of the card will need to include the firm's name (logo), website url, and phone number. It will also need to include, at the very least, the name of the attorney, the attorney's title, the attorney's email address, and the attorney's twitter feed. (I do not maintain a dedicated office and therefore the card does not need to specify a business address.) I will provide the actual contact information to the winning designer. Until then, you may use fictional data in suggesting your proposed design.

My firm specializes in representing startup companies. This means I routinely interact with young entrepreneurs and the (typically) older, more experienced investors who fund them. I need to appeal to the former without offending the latter. I'm interesting in conveying the idea that my firm is a credible alternative to larger, brand-name firms. I use these words in positioning my firm in this market: creative; flexible; fair; practical; experienced. The winning design needs to convey this idea.

I'm will also be re-working my website soon and will likely use noto sans and noto serif as my primary website fonts. I'd like the business card to use a font that is similar, but also compatible with the font used in the firm's logo.

Target Market(s)

Young entrepreneurs and older investors who collaborate in the formation and funding of high-tech startup companies located in the Pacific Northwest.

Industry/Entity Type

Law Firm

Font styles to use
Serif
Sans Serif

Requirements
Must have
• Firm logo, firm tag line, firm website url, firm phone number, attorney name, attorney title, attorney email address, and attorney twitter.

The attached pdf indicates kind of what I have in mind, recognizing that it is my amateur attempt at doing what I'm hoping the winning designer is able to do so much better.
Nice to have
• Adding a statement about my practice areas, if there's room, might be nice:

"General Counsel | Business Formation | Intellectual Property | Angel Investments & Venture Capital | Mergers & Acquisitions"

Also, I make it a point to meet with clients "by appointment only" in the following areas of Seattle: "Freemont | Pioneer Square | Redmond | South Lake Union." It might be worth including as well, but only if the card itself isn't too cramped. I favor "too simple" over "too informative."
Should not have
• Do NOT put the scales of justice anywhere on this business card. I am a business lawyer.

```html
<!DOCTYPE html>
<html lang="en">
<head>
<meta charset="utf-8">
<title>Brockwyn Law PLLC – Business Card</title>
<link rel="stylesheet" href="https://fonts.googleapis.com/css2?family=Noto+Sans:wght@400;600;700&display=swap">
<style>
  :root {
    --navy: #1f4a82;
    --navy-deep: #183c6c;
    --ink: #23477a;
    --grey: #8a8f97;
    --paper: #ffffff;
    --backdrop: #e6e7ea;
  }
  * { box-sizing: border-box; margin: 0; padding: 0; }
  html, body { width: 1200px; height: 873px; overflow: hidden; }
  body {
    background: var(--backdrop);
    font-family: "Noto Sans", sans-serif;
    color: var(--ink);
    position: relative;
  }
  .card {
    position: absolute;
    top: 288px;
    width: 520px;
    height: 297px;
    background: var(--paper);
    box-shadow: 0 6px 18px rgba(0,0,0,.18);
    overflow: hidden;
  }
  .card--face { left: 55px; }
  .card--back { left: 625px; }

  /* face */
  .practice-areas {
    position: absolute; left: 34px; top: 26px;
    font-size: 10.5px; line-height: 1.4; color: var(--ink);
  }
  .brand { position: absolute; left: 34px; top: 74px; }
  .brand__name {
    display: flex; align-items: center; gap: 7px;
    font-size: 21px; font-weight: 400; letter-spacing: 1.5px; color: var(--ink);
  }
  .brand__square { width: 11px; height: 11px; background: var(--navy); }
  .brand__tagline {
    margin-top: 2px; font-size: 6.8px; letter-spacing: 1.3px; color: var(--grey);
  }
  .contact { position: absolute; left: 34px; top: 138px; list-style: none; }
  .contact li {
    display: flex; align-items: center; gap: 9px;
    font-size: 10.5px; height: 19px; color: var(--ink);
  }
  .contact svg { width: 12px; height: 12px; fill: var(--ink); flex: none; }
  .attorney { position: absolute; right: 40px; top: 150px; text-align: left; }
  .attorney__name { font-size: 21px; font-weight: 700; letter-spacing: .5px; color: var(--ink); }
  .attorney__title { font-size: 12px; color: var(--ink); padding-left: 36px; }
  .locations {
    position: absolute; left: 0; right: 0; bottom: 0; height: 36px;
    background: var(--navy); color: #fff;
    font-size: 10.5px; display: flex; align-items: center; padding-left: 34px;
    letter-spacing: .3px;
  }

  /* back */
  .card--back { background: var(--navy); }
  .back__band {
    position: absolute; left: 0; right: 0; top: 74px; height: 150px;
    background: var(--paper);
    display: flex; flex-direction: column; justify-content: center; padding-left: 150px;
  }
  .back__band .brand__name { font-size: 26px; letter-spacing: 2px; }
  .back__band .brand__square { width: 14px; height: 14px; }
  .back__band .brand__tagline { font-size: 8px; letter-spacing: 1.6px; margin-top: 4px; }
</style>
</head>
<body>

<section class="card card--face" aria-label="Card front">
  <p class="practice-areas">General Counsel | Business Formation | Intellectual Property<br>Angel Investments &amp; Venture Capital | Mergers &amp; Acquisitions</p>

  <div class="brand">
    <div class="brand__name"><span class="brand__square"></span>BROCKWYN LAW PLLC</div>
    <div class="brand__tagline">COUNSEL FOR THE INNOVATIVE COMPANY</div>
  </div>

  <ul class="contact">
    <li>
      <svg viewBox="0 0 24 24" aria-hidden="true"><path d="M6.6 10.8a15.5 15.5 0 0 0 6.6 6.6l2.2-2.2a1 1 0 0 1 1-.25 11.4 11.4 0 0 0 3.6.57 1 1 0 0 1 1 1V20a1 1 0 0 1-1 1A17 17 0 0 1 3 4a1 1 0 0 1 1-1h3.5a1 1 0 0 1 1 1c0 1.25.2 2.45.57 3.57a1 1 0 0 1-.25 1z"/></svg>
      555 - 014 - 2278
    </li>
    <li>
      <svg viewBox="0 0 24 24" aria-hidden="true"><path d="M12 2a10 10 0 1 0 0 20 10 10 0 0 0 0-20zm6.9 6h-2.9a15.7 15.7 0 0 0-1.4-3.6A8 8 0 0 1 18.9 8zM12 4a14 14 0 0 1 1.9 4h-3.8A14 14 0 0 1 12 4zM4.3 14a8 8 0 0 1 0-4h3.4a16.5 16.5 0 0 0 0 4zm.8 2h2.9a15.7 15.7 0 0 0 1.4 3.6A8 8 0 0 1 5.1 16zM8 8H5.1a8 8 0 0 1 4.3-3.6A15.7 15.7 0 0 0 8 8zm4 12a14 14 0 0 1-1.9-4h3.8A14 14 0 0 1 12 20zm2.3-6H9.7a14.7 14.7 0 0 1 0-4h4.6a14.7 14.7 0 0 1 0 4zm.3 5.6a15.7 15.7 0 0 0 1.4-3.6h2.9a8 8 0 0 1-4.3 3.6zM16.3 14a16.5 16.5 0 0 0 0-4h3.4a8 8 0 0 1 0 4z"/></svg>
      www.brockwynlaw.com
    </li>
    <li><span style="width:12px"></span>info@brockwynlaw.com</li>
    <li>
      <svg viewBox="0 0 24 24" aria-hidden="true"><circle cx="12" cy="12" r="9"/></svg>
      @OWENBROCKWYN
    </li>
  </ul>

  <div class="attorney">
    <div class="attorney__name">OWEN BROCKWYN</div>
    <div class="attorney__title">Startup Attorney</div>
  </div>

  <div class="locations">Freemont | Pioneer Square | Redmond | South Lake Union</div>
</section>

<section class="card card--back" aria-label="Card back">
  <div class="back__band">
    <div class="brand__name"><span class="brand__square"></span>BROCKWYN LAW PLLC</div>
    <div class="brand__tagline">COUNSEL FOR THE INNOVATIVE COMPANY</div>
  </div>
</section>

</body>
</html>
```